Business Card Design

We need a business card designed to the point of print ready to take to our printers. the design should be professional, easy to read and simple. The cards should represent our business as professional and trust worthy.

Attached are several versions o the logo, and also the details for the card to be printed. please do communicate if different versions of the logo is required.

Business

```html
<!DOCTYPE html>
<html lang="en">
<head>
<meta charset="utf-8">
<title>Northgate Recoveries Business Card</title>
<link href="https://fonts.googleapis.com/css2?family=Exo+2:wght@400;500;600;700&display=swap" rel="stylesheet">
<style>
  :root {
    --orange: #f29a1f;
    --orange-deep: #e8890f;
    --ink: #505050;
    --ink-soft: #666666;
    --paper: #ffffff;
    --paper-shade: #ececec;
    --backdrop: #2b2b2b;
  }
  * { margin: 0; padding: 0; box-sizing: border-box; }
  html, body { width: 1200px; height: 900px; overflow: hidden; }
  body {
    background: var(--backdrop);
    font-family: "Exo 2", Arial, sans-serif;
    display: flex;
    align-items: center;
    justify-content: center;
    gap: 60px;
  }
  .card {
    position: relative;
    width: 540px;
    height: 330px;
    border-radius: 24px;
    overflow: hidden;
  }
  .card--front {
    background: linear-gradient(160deg, var(--paper) 40%, var(--paper-shade));
    color: var(--ink);
  }
  .card__band { position: absolute; inset: 0; }
  .company {
    position: absolute;
    left: 36px;
    top: 42px;
    font-weight: 600;
    font-size: 28px;
    color: var(--ink);
  }
  .person { position: absolute; left: 36px; top: 140px; }
  .person__name { font-size: 22px; font-weight: 600; color: var(--orange); }
  .person__role { font-size: 15px; color: var(--ink-soft); margin-top: 2px; }
  .contact { position: absolute; left: 36px; top: 200px; font-size: 16px; color: var(--ink); }
  .contact__row { display: flex; align-items: center; gap: 8px; height: 25px; }
  .icon { width: 14px; height: 14px; flex: none; }
  .address {
    position: absolute;
    left: 336px;
    top: 128px;
    font-size: 14px;
    color: var(--ink);
    display: flex;
    gap: 8px;
    line-height: 1.45;
  }
  .address .icon { margin-top: 3px; }
  .web {
    position: absolute;
    left: 36px;
    bottom: 17px;
    display: flex;
    align-items: center;
    gap: 8px;
    color: var(--paper);
    font-size: 16px;
  }
  .card--back {
    background: linear-gradient(160deg, var(--orange) 30%, var(--orange-deep));
  }
  .card--back .company {
    left: auto;
    top: auto;
    right: 34px;
    bottom: 40px;
    color: var(--paper);
  }
</style>
</head>
<body>
  <div class="card card--front">
    <svg class="card__band" viewBox="0 0 540 330" aria-hidden="true">
      <polygon points="0,278 290,278 540,214 540,330 0,330" fill="var(--orange)"/>
      <line x1="300" y1="268" x2="540" y2="206" stroke="var(--orange)" stroke-width="1.5"/>
      <line x1="320" y1="259" x2="540" y2="199" stroke="var(--orange)" stroke-width="1"/>
    </svg>

    <div class="company">Northgate Recoveries</div>

    <div class="person">
      <div class="person__name">Dana Whitfield</div>
      <div class="person__role">Managing Director</div>
    </div>

    <div class="contact">
      <div class="contact__row">
        <svg class="icon" viewBox="0 0 16 16" aria-hidden="true"><circle cx="8" cy="8" r="7" fill="none" stroke="var(--orange)" stroke-width="1.5"/><path d="M5.5 4.5l1.5 0 .8 2-1 .8a5 5 0 0 0 2 2l.8-1 2 .8v1.5c0 .5-.5 1-1 1A6.5 6.5 0 0 1 4.5 5.5c0-.5.5-1 1-1z" fill="var(--orange)"/></svg>
        <span>+61 400 555 019</span>
      </div>
      <div class="contact__row">
        <svg class="icon" viewBox="0 0 16 16" aria-hidden="true"><rect x="1" y="3" width="14" height="10" fill="var(--orange)"/><path d="M1 3l7 6 7-6" fill="none" stroke="var(--paper)" stroke-width="1.2"/></svg>
        <span>dana@northgaterecoveries.com.au</span>
      </div>
    </div>

    <div class="address">
      <svg class="icon" viewBox="0 0 16 16" aria-hidden="true"><path d="M8 1.5L1 8h2v6.5h4v-4h2v4h4V8h2z" fill="var(--orange)"/></svg>
      <div>PO Box 7721 Q<br>Harbourside Qld 4400</div>
    </div>

    <div class="web">
      <svg class="icon" viewBox="0 0 16 16" aria-hidden="true"><g fill="none" stroke="var(--paper)" stroke-width="1.2"><circle cx="8" cy="8" r="6.5"/><ellipse cx="8" cy="8" rx="3" ry="6.5"/><line x1="1.5" y1="8" x2="14.5" y2="8"/></g></svg>
      <span>www.northgaterecoveries.com.au</span>
    </div>
  </div>

  <div class="card card--back">
    <div class="company">Northgate Recoveries</div>
  </div>
</body>
</html>
```